Optometrist Window poster "Retinal Photography Bulk Billed"

We are an optometry practice and we need a poster to highlight that we Bulk Bill retinal photography as part of the eye exam so there is no extra charge.

I've uploaded a Retinal Photograph which would need to be displayed in the poster.

The artwork will be displayed as a fabric banner in our shop window. We have 7 other banners with different services our business provides. The words needs to standout for passers by and the cars stopped at the traffic lights out front of our business. We already have signs with our logos phone number etc. so we won't need them included in the poster.

The size will be 1300mm width x 1900mm height

The Poster will need to say:
Have you had your photo taken?
Retinal Photography Bulk Billed

Target Market(s)

Passes by and cars stopped at traffic lights.

Industry/Entity Type

Optician

Requirements
Must have
• Have you had your photo taken?
• Retinal Photography Bulk Billed
• A Retinal Photograph

```html
<!DOCTYPE html>
<html lang="en">
<head>
<meta charset="utf-8">
<title>Retinal Photography Bulk Billed – Window Banner</title>
<link rel="stylesheet" href="https://fonts.googleapis.com/css2?family=Josefin+Sans:wght@300;400&family=Bodoni+Moda:opsz,wght@6..96,700&display=swap">
<style>
  :root {
    --page-bg: #f2f2f2;
    --banner-black: #030303;
    --headline-red: #c8161d;
    --lead-salmon: #e8766a;
    --detail-pink: #f2a193;
    --retina-light: #ec6a4a;
    --retina-dark: #d04a32;
  }
  html, body {
    margin: 0;
    width: 1200px;
    height: 900px;
    overflow: hidden;
    background: var(--page-bg);
  }
  .banner {
    position: absolute;
    left: 420px;
    top: 30px;
    width: 360px;
    height: 840px;
    background: var(--banner-black);
    overflow: hidden;
    box-shadow: 0 6px 24px rgba(0,0,0,0.18);
  }
  .retina-photo {
    position: absolute;
    left: -10px;
    top: -96px;
    width: 380px;
    height: 380px;
    border-radius: 50%;
    background: radial-gradient(circle at 50% 40%, var(--retina-light), var(--retina-dark));
  }
  .message {
    position: absolute;
    left: 0;
    right: 0;
    top: 318px;
    text-align: center;
  }
  .lead-line {
    margin: 0;
    font-family: "Josefin Sans", sans-serif;
    font-weight: 300;
    font-size: 20px;
    letter-spacing: -0.4px;
    color: var(--lead-salmon);
    line-height: 1;
  }
  .headline {
    margin: 4px 0 0;
    font-family: "Bodoni Moda", serif;
    font-weight: 700;
    font-size: 64px;
    line-height: 0.84;
    color: var(--headline-red);
    transform: scaleX(0.78);
    letter-spacing: 1px;
  }
  .service {
    margin: 36px 0 0;
    font-family: "Josefin Sans", sans-serif;
    font-weight: 400;
    font-size: 17px;
    line-height: 1.3;
    color: var(--detail-pink);
    letter-spacing: 0.2px;
  }
</style>
</head>
<body>
  <main class="banner">
    <div class="retina-photo" role="img" aria-label="Retinal photograph of the back of the eye"></div>
    <div class="message">
      <p class="lead-line">HAVE YOU HAD YOUR</p>
      <h1 class="headline">PHOTO<br>TAKEN?</h1>
      <p class="service">RETINAL PHOTOGRAPHY<br>BULK BILLED</p>
    </div>
  </main>
</body>
</html>
```